Cannabis Company needs a packaging design for a 4x6 pouch

We need a design for a new cannabis company. Included is the logo in red. The logo color can change. Whatever color looks best with the design is what we'll use. The design can't include any cartoon characters or anything that may appeal to children. We have multiple products that are similar that will be using the same design. The pouch will contain 10 pyramid shaped gummies. The look we're going for is modern, simple, but eye catching. I included a handful of photos of packaging we like if that helps.

```html
<!DOCTYPE html>
<html lang="en">
<head>
<meta charset="utf-8">
<title>Lumora Delta-10 THC Gummies – Pouch Front</title>
<link rel="stylesheet" href="https://fonts.googleapis.com/css2?family=Montserrat:wght@500;600;700;800&family=Barlow+Semi+Condensed:wght@400;500&family=Allura&display=swap">
<style>
  :root {
    --bg: #f4f5f7;
    --navy: #1c2557;
    --navy-deep: #151c46;
    --navy-line: #2a3470;
    --sky: #6f9ae0;
    --sky-soft: #8fb3ec;
    --white: #ffffff;
    --rule: rgba(255,255,255,0.55);
  }
  * { margin: 0; padding: 0; box-sizing: border-box; }
  html, body { width: 1200px; height: 1200px; overflow: hidden; background: var(--bg); }
  .canvas { position: relative; width: 1200px; height: 1200px; }

  .pouch {
    position: absolute; left: 300px; top: 130px; width: 600px; height: 940px;
    background: linear-gradient(180deg, var(--navy) 0%, var(--navy-deep) 100%);
    border-radius: 6px;
    box-shadow: 0 30px 60px rgba(20,28,70,0.25);
    overflow: hidden;
  }
  .pouch-seal {
    position: absolute; left: 0; right: 0; top: 0; height: 60px;
    border-bottom: 2px solid var(--navy-line);
  }
  .pouch-zipper {
    position: absolute; left: 0; right: 0; top: 150px; height: 10px;
    border-top: 2px solid var(--navy-line); border-bottom: 2px solid var(--navy-line);
  }
  .tear-notch {
    position: absolute; top: 96px; width: 12px; height: 18px; background: var(--bg);
    border-radius: 0 9px 9px 0;
  }
  .tear-notch.left { left: 0; }
  .tear-notch.right { right: 0; border-radius: 9px 0 0 9px; }

  .claims {
    position: absolute; top: 250px; left: 60px; right: 60px;
    display: flex; justify-content: space-between;
    font-family: "Barlow Semi Condensed", sans-serif; font-weight: 400;
    font-size: 21px; letter-spacing: 0.5px; color: var(--white);
  }
  .claim { display: flex; flex-direction: column; align-items: center; gap: 10px; width: 150px; }
  .claim svg { width: 30px; height: 30px; }

  .brand {
    position: absolute; top: 420px; left: 0; right: 0;
    display: flex; flex-direction: column; align-items: center;
  }
  .brand-box {
    border: 2px solid var(--rule); padding: 26px 36px 20px;
    display: flex; flex-direction: column; align-items: center;
  }
  .brand-name {
    display: flex; align-items: center; gap: 12px;
    font-family: "Montserrat", sans-serif; font-weight: 600; font-size: 52px;
    color: var(--white); line-height: 1; letter-spacing: -1px;
  }
  .brand-dot { width: 14px; height: 14px; border-radius: 50%; background: var(--white); }
  .brand-tag {
    margin-top: 8px; font-family: "Montserrat", sans-serif; font-weight: 500;
    font-size: 13px; letter-spacing: 3px; color: var(--white);
  }

  .product-title { position: absolute; top: 618px; left: 0; right: 0; text-align: center; font-family: "Montserrat", sans-serif; }
  .product-kind { font-weight: 700; font-size: 46px; color: var(--sky); letter-spacing: 1px; line-height: 1; }
  .product-form { font-weight: 800; font-size: 86px; color: var(--white); line-height: 1.05; letter-spacing: 1px; }

  .flavor-art {
    position: absolute; top: 780px; left: 272px; width: 56px; height: 60px;
    border-radius: 50%; background: radial-gradient(circle, #3b4a8c 0%, var(--navy) 75%);
  }
  .flavor-name {
    position: absolute; top: 830px; left: 0; right: 0; text-align: center;
    font-family: "Allura", cursive; font-size: 64px; color: var(--sky); line-height: 1;
  }
  .dose {
    position: absolute; top: 902px; left: 0; right: 0; text-align: center;
    font-family: "Barlow Semi Condensed", sans-serif; font-weight: 500; font-size: 22px; color: var(--white);
  }
  .dose .accent { color: var(--sky-soft); }
</style>
</head>
<body>
<main class="canvas">
  <section class="pouch" aria-label="Delta-10 THC gummies pouch, front">
    <div class="pouch-seal"></div>
    <span class="tear-notch left"></span>
    <span class="tear-notch right"></span>
    <div class="pouch-zipper"></div>

    <ul class="claims">
      <li class="claim">
        <svg viewBox="0 0 30 30" fill="none" stroke="#8fb3ec" stroke-width="1.6"><circle cx="15" cy="15" r="13"/><line x1="6" y1="24" x2="24" y2="6"/></svg>
        GLUTEN FREE
      </li>
      <li class="claim">
        <svg viewBox="0 0 30 30" fill="none" stroke="#8fb3ec" stroke-width="1.6"><circle cx="15" cy="15" r="13"/><line x1="6" y1="24" x2="24" y2="6"/></svg>
        NON-GMO
      </li>
      <li class="claim">
        <svg viewBox="0 0 30 30" fill="none" stroke="#8fb3ec" stroke-width="1.6"><circle cx="15" cy="15" r="13"/><line x1="6" y1="24" x2="24" y2="6"/></svg>
        FAT FREE
      </li>
    </ul>

    <div class="brand">
      <div class="brand-box">
        <div class="brand-name"><span class="brand-dot"></span>lumora</div>
        <div class="brand-tag">CANNABIS COMPANY</div>
      </div>
    </div>

    <h1 class="product-title">
      <div class="product-kind">DELTA-10 THC</div>
      <div class="product-form">GUMMIES</div>
    </h1>

    <div class="flavor-art" role="img" aria-label="Small line illustration of a blueberry cluster"></div>
    <p class="flavor-name">Blueberry</p>
    <p class="dose"><span class="accent">25MG DELTA</span> 10 PER GUMMY</p>
  </section>
</main>
</body>
</html>
```